Sales Process

I need a card/page to hand out to my new clients that gives them an over view of our sales process start to finish. Along with 3 points that set us apart from all other competition.
The attached file is my first attempt with other ideas so give your suggestions.
Check out my website to get an idea of who we are. www.brightmeadowyards.com

```html
<!DOCTYPE html>
<html lang="en">
<head>
<meta charset="utf-8">
<title>Bright Meadow Yards – Why Choose Us & Our Process</title>
<link rel="stylesheet" href="https://fonts.googleapis.com/css2?family=Nunito+Sans:ital,wght@0,400;0,700;0,800;1,400&family=Raleway:wght@400;500&display=swap">
<style>
  :root {
    --green: #96c85a;
    --ink: #4a4a4c;
    --ink-soft: #555557;
    --footer: #58585a;
    --paper: #ffffff;
  }
  * { margin: 0; padding: 0; box-sizing: border-box; }
  html, body { width: 1200px; height: 733px; overflow: hidden; background: var(--paper); }
  .page { position: relative; width: 1200px; height: 733px; color: var(--ink); font-family: "Raleway", sans-serif; }

  .section-title { position: absolute; font-family: "Nunito Sans", sans-serif; font-weight: 800; font-size: 37px; letter-spacing: -0.5px; color: var(--ink); }
  .why-title { left: 76px; top: 32px; }

  .feature { position: absolute; left: 68px; width: 600px; height: 70px; }
  .feature-icon { position: absolute; left: 0; top: 2px; width: 54px; height: 54px; }
  .feature-name { position: absolute; left: 73px; top: 0; font-family: "Nunito Sans", sans-serif; font-weight: 700; font-size: 26px; line-height: 30px; color: var(--ink); }
  .feature-text { position: absolute; left: 73px; top: 34px; font-size: 20px; line-height: 24px; color: var(--ink-soft); white-space: nowrap; }
  .feature-star { top: 104px; }
  .feature-design { top: 186px; }
  .feature-trust { top: 271px; }

  .brand { position: absolute; left: 730px; top: 70px; width: 400px; height: 230px; text-align: center; }
  .brand-mark { display: block; width: 26px; height: 26px; border-radius: 50%; background: var(--green); margin: 40px auto 18px; }
  .brand-name { font-family: "Nunito Sans", sans-serif; font-weight: 800; font-size: 40px; line-height: 46px; color: var(--ink); letter-spacing: 1px; }
  .brand-tagline { margin-top: 34px; font-family: "Nunito Sans", sans-serif; font-style: italic; font-size: 19px; color: var(--ink); }

  .process-title { left: 0; width: 1200px; top: 362px; text-align: center; }
  .divider { position: absolute; top: 386px; height: 0; border-top: 2px dashed var(--ink); }
  .divider-left { left: 77px; width: 403px; }
  .divider-right { left: 722px; width: 402px; }

  .step { position: absolute; top: 453px; width: 190px; height: 190px; border-radius: 50%; background: var(--paper); box-shadow: 0 6px 22px rgba(0,0,0,0.16); text-align: center; }
  .step-icon { position: absolute; left: 50%; top: 28px; width: 52px; height: 52px; transform: translateX(-50%); }
  .step-label { position: absolute; left: 0; right: 0; top: 100px; font-family: "Nunito Sans", sans-serif; font-size: 18px; line-height: 23px; color: var(--ink); }
  .step-label strong { font-weight: 800; display: block; }
  .step-complete .step-label { top: 80px; line-height: 21.5px; }
  .step-1 { left: 74px; } .step-2 { left: 290px; } .step-3 { left: 505px; } .step-4 { left: 721px; } .step-5 { left: 936px; }

  .chevron { position: absolute; top: 530px; width: 36px; height: 44px; z-index: 2; }
  .chevron-1 { left: 271px; } .chevron-2 { left: 487px; } .chevron-3 { left: 703px; } .chevron-4 { left: 918px; }

  .celebrate-spot { position: absolute; left: 50%; top: 22px; width: 56px; height: 56px; transform: translateX(-50%); border-radius: 50%; background: linear-gradient(#5a5a5c, #4a4a4c); }

  .footer-accent { position: absolute; left: 0; top: 689px; width: 1200px; height: 8px; background: var(--green); }
  .footer-bar { position: absolute; left: 0; top: 697px; width: 1200px; height: 36px; background: var(--footer); }
</style>
</head>
<body>
<main class="page">
  <h1 class="section-title why-title">Why Choose Us?</h1>

  <div class="feature feature-star">
    <svg class="feature-icon" viewBox="0 0 54 54" aria-hidden="true">
      <polygon fill="var(--green)" points="28,4 34,21 51,21 37,31 42,48 28,38 14,48 19,31 5,21 22,21"/>
    </svg>
    <h2 class="feature-name">5 Star Experience</h2>
    <p class="feature-text">We want you to be thrilled with your outdoor space.</p>
  </div>

  <div class="feature feature-design">
    <svg class="feature-icon" viewBox="0 0 54 54" aria-hidden="true">
      <g fill="var(--green)">
        <circle cx="27" cy="19" r="15"/>
        <rect x="19" y="31" width="16" height="10" rx="2"/>
        <rect x="21" y="43" width="12" height="4" rx="2"/>
      </g>
      <path d="M24 34 V16 L27 10 L30 16 V34" fill="none" stroke="#fff" stroke-width="2.4"/>
      <g stroke="var(--green)" stroke-width="2.6" stroke-linecap="round">
        <line x1="3" y1="18" x2="7" y2="18"/><line x1="47" y1="18" x2="51" y2="18"/>
        <line x1="5" y1="8" x2="8" y2="10"/><line x1="49" y1="8" x2="46" y2="10"/>
        <line x1="5" y1="28" x2="8" y2="26"/><line x1="49" y1="28" x2="46" y2="26"/>
      </g>
    </svg>
    <h2 class="feature-name">Creative Custom Design</h2>
    <p class="feature-text">Every project is taylored to provide the RIGHT space.</p>
  </div>

  <div class="feature feature-trust">
    <svg class="feature-icon" viewBox="0 0 54 54" aria-hidden="true">
      <path d="M27 2 L45 9 V28 C45 40 36 47 27 52 C18 47 9 40 9 28 V9 Z" fill="var(--green)"/>
      <polyline points="18,28 25,34 37,21" fill="none" stroke="#fff" stroke-width="3.4" stroke-linecap="round" stroke-linejoin="round"/>
    </svg>
    <h2 class="feature-name">Trustworthy</h2>
    <p class="feature-text">We keep our word.</p>
  </div>

  <div class="brand">
    <span class="brand-mark" aria-hidden="true"></span>
    <p class="brand-name">BRIGHT MEADOW<br>YARDS</p>
    <p class="brand-tagline">Creating Exceptional Outdoor Living Spaces</p>
  </div>

  <span class="divider divider-left" aria-hidden="true"></span>
  <h2 class="section-title process-title">Our Process</h2>
  <span class="divider divider-right" aria-hidden="true"></span>

  <section class="step step-1">
    <svg class="step-icon" viewBox="0 0 52 52" aria-hidden="true">
      <path d="M8 6 C5 8 4 12 6 17 C11 29 21 39 33 45 C38 47 42 46 45 42 L46 40 C47 38 46 36 44 35 L37 31 C35 30 33 31 32 32 L29 35 C23 32 18 27 15 21 L18 18 C19 17 20 15 19 13 L15 6 C14 4 12 3 10 4 Z" fill="var(--ink)"/>
      <g fill="none" stroke="var(--ink)" stroke-width="3" stroke-linecap="round">
        <path d="M28 14 A9 9 0 0 1 37 23"/><path d="M29 6 A17 17 0 0 1 45 22"/>
      </g>
    </svg>
    <p class="step-label"><strong>Initial Call</strong>How can we<br>help?</p>
  </section>

  <svg class="chevron chevron-1" viewBox="0 0 36 44" aria-hidden="true"><polygon points="0,0 14,0 36,22 14,44 0,44 22,22" fill="var(--green)"/></svg>

  <section class="step step-2">
    <svg class="step-icon" viewBox="0 0 52 52" aria-hidden="true">
      <g fill="var(--ink)">
        <ellipse cx="24" cy="10" rx="12" ry="9"/>
        <circle cx="12" cy="28" r="4"/><circle cx="26" cy="26" r="4.5"/><circle cx="40" cy="28" r="4"/>
        <rect x="5" y="34" width="14" height="14" rx="4"/>
        <rect x="19" y="32" width="14" height="16" rx="4"/>
        <rect x="33" y="34" width="14" height="14" rx="4"/>
        <rect x="2" y="40" width="48" height="3"/>
      </g>
      <g fill="#fff"><circle cx="19" cy="10" r="1.6"/><circle cx="24" cy="10" r="1.6"/><circle cx="29" cy="10" r="1.6"/></g>
    </svg>
    <p class="step-label"><strong>Site Visit</strong>Dream, Plan,<br>Design</p>
  </section>

  <svg class="chevron chevron-2" viewBox="0 0 36 44" aria-hidden="true"><polygon points="0,0 14,0 36,22 14,44 0,44 22,22" fill="var(--green)"/></svg>

  <section class="step step-3">
    <svg class="step-icon" viewBox="0 0 52 52" aria-hidden="true">
      <path d="M8 4 H28 L38 14 V44 H8 Z" fill="var(--ink)"/>
      <g stroke="#fff" stroke-width="2.6" stroke-linecap="round">
        <line x1="14" y1="18" x2="24" y2="18"/><line x1="14" y1="25" x2="22" y2="25"/><line x1="14" y1="32" x2="20" y2="32"/>
      </g>
      <circle cx="38" cy="38" r="11" fill="var(--ink)" stroke="#fff" stroke-width="2.5"/>
      <polyline points="33,38 37,42 43,34" fill="none" stroke="#fff" stroke-width="2.4" stroke-linecap="round" stroke-linejoin="round"/>
    </svg>
    <p class="step-label"><strong>Design</strong>Proposal</p>
  </section>

  <svg class="chevron chevron-3" viewBox="0 0 36 44" aria-hidden="true"><polygon points="0,0 14,0 36,22 14,44 0,44 22,22" fill="var(--green)"/></svg>

  <section class="step step-4">
    <svg class="step-icon" viewBox="0 0 52 52" aria-hidden="true">
      <g fill="var(--ink)">
        <path d="M6 24 C6 12 15 4 26 4 C37 4 46 12 46 24 Z"/>
        <rect x="3" y="24" width="46" height="6" rx="2"/>
        <path d="M13 33 H39 C39 42 33 48 26 48 C19 48 13 42 13 33 Z"/>
      </g>
      <g stroke="#fff" stroke-width="2.6"><line x1="20" y1="5" x2="18" y2="22"/><line x1="32" y1="5" x2="34" y2="22"/></g>
      <circle cx="26" cy="38" r="5" fill="#fff"/>
    </svg>
    <p class="step-label"><strong>Installation</strong>Construction</p>
  </section>

  <svg class="chevron chevron-4" viewBox="0 0 36 44" aria-hidden="true"><polygon points="0,0 14,0 36,22 14,44 0,44 22,22" fill="var(--green)"/></svg>

  <section class="step step-5 step-complete">
    <div class="celebrate-spot" role="img" aria-label="Icon of a cheering client celebrating the finished project"></div>
    <p class="step-label"><strong>Complete</strong>Kick back and<br>relax a smile on<br>your face</p>
  </section>

  <div class="footer-accent" aria-hidden="true"></div>
  <div class="footer-bar" aria-hidden="true"></div>
</main>
</body>
</html>
```